Design Brief: Tidewell Group Business Card Design
Project Overview

Tidewell Group is a strategic partner to entrepreneurs and leadership teams, supporting business growth through clarity, execution, and trusted expertise. We are looking for a premium, modern business card design that reflects confidence, professionalism, and upward momentum.

Main logo the one with gold bar for the Tidewell Group.

This card will be used by executives and staff across the Tidewell Group business.

Brand Personality
Professional but human
Confident but collaborative
Strategic, credible, and execution-focused
Premium without being flashy

This is not a startup, tech gimmick, or overly creative brand.

Card Format
Portrait orientation (vertical)
Standard size: 55 × 90 mm
Two-sided
One corner cut (top-right corner preferred) to subtly represent upward movement and growth

Design must still work if corner cutting is not available with certain printers

Front Side (Contact Details)
Include:
Tidewell Group logo (provided)
Name
Title
Phone number
Email address
Website
Optional: tagline at the bottom

Style:
Clean
Minimal
Plenty of white space
Easy to read

Back Side (Ecosystem / Brand Message)
Include:
Heading such as: “The Tidewell Network”
Short 2–3 line description explaining that Tidewell unites a connected group of specialist professional advisory firms delivering expertise operating across Strategic Advisory, Capital Raising, People, & Finance.

This side should reinforce scale, capability, and partnership, not sales messaging.

Colours
Primary brand colours:
Tidewell Blue: #0063B0
Deep Blue: #1A3D6D
Gold accent (very subtle use only): #C9A24D

Rules:
No gradients
No bright or neon colours
No heavy textures
Gold should be minimal and refined

Typography
Clean, modern sans-serif
Professional and readable
No script or decorative fonts

What to Avoid
Landscape layouts (Unless recommended based on logo design, which is horizontal in nature)
Overdesigned or cluttered cards
Loud colours or gradients
Trendy effects that won’t age well

Multiple accent colours

Deliverables
Print-ready files (PDF)
Editable source files (AI / PSD)
Front and back designs

Mockups showing the portrait card and cut corner

Target Outcome
A business card that feels:
Executive
Distinctive
Timeless
Aligned to a strategic, multi-division business

Target Market(s)

Business Owners and Executives (Across industries)

Industry/Entity Type

Professional Services

Contact Information for Business Card

First name and Surname, Email address, Cell phone number, website

Font styles to use
Other font styles liked:
• IBM Plex Sans and or Sans Pro

Colors
0054AA
0677BA
7BADD7
CADEEF
E8F1F8

Requirements
Must have
• Include QR code to digital business card.

```html
<!DOCTYPE html>
<html lang="en">
<head>
<meta charset="utf-8">
<title>Tidewell Group – Business Card</title>
<link href="https://fonts.googleapis.com/css2?family=Poppins:wght@400;600;700&family=Open+Sans:ital,wght@1,600&display=swap" rel="stylesheet">
<style>
  :root {
    --canvas: #b7b7b7;
    --deep-blue: #1b3c6b;
    --tidewell-blue: #0063b0;
    --gold: #c09a22;
    --white: #ffffff;
    --ink: #111111;
    --rule-grey: #8a8a8a;
  }
  html, body {
    margin: 0;
    padding: 0;
    width: 1200px;
    height: 1200px;
    overflow: hidden;
    background: var(--canvas);
  }
  .canvas {
    position: relative;
    width: 1200px;
    height: 1200px;
    font-family: "Poppins", Arial, sans-serif;
  }
  .card {
    position: absolute;
    top: 303px;
    width: 367px;
    height: 594px;
    box-shadow: 4px 4px 4px rgba(0,0,0,0.45);
  }
  .card--back {
    left: 202px;
    background: var(--deep-blue);
    border-top-left-radius: 105px;
  }
  .card--front {
    left: 599px;
    background: var(--white);
    border-top-right-radius: 105px;
  }

  /* Back side */
  .network-heading {
    position: absolute;
    top: 226px;
    left: 0;
    width: 100%;
    margin: 0;
    text-align: center;
    color: var(--gold);
    font-weight: 600;
    font-size: 25px;
    letter-spacing: 0.2px;
  }
  .network-rule {
    position: absolute;
    left: 38px;
    width: 291px;
    height: 1px;
    background: var(--tidewell-blue);
  }
  .network-rule--top { top: 301px; }
  .network-rule--bottom { top: 531px; }
  .network-description {
    position: absolute;
    top: 310px;
    left: 10px;
    width: 347px;
    margin: 0;
    text-align: center;
    color: var(--white);
    font-weight: 600;
    font-size: 20px;
    line-height: 29.2px;
    white-space: nowrap;
  }

  /* Front side */
  .brand {
    position: absolute;
    top: 94px;
    left: 90px;
    display: flex;
    align-items: flex-start;
    gap: 15px;
  }
  .brand-mark {
    width: 16px;
    height: 16px;
    margin-top: 8px;
    background: var(--gold);
  }
  .brand-name {
    margin: 0;
    color: var(--ink);
    font-weight: 700;
    font-size: 32px;
    line-height: 32px;
    letter-spacing: 0.5px;
  }
  .brand-tagline {
    margin: 6px 0 0;
    font-family: "Open Sans", Arial, sans-serif;
    font-style: italic;
    font-weight: 600;
    font-size: 11.3px;
    line-height: 13px;
    color: var(--ink);
    white-space: nowrap;
  }
  .person {
    position: absolute;
    top: 386px;
    left: 0;
    width: 100%;
    text-align: center;
  }
  .person-name {
    margin: 0;
    color: var(--tidewell-blue);
    font-weight: 700;
    font-size: 27px;
    line-height: 30px;
  }
  .person-title {
    margin: 0;
    color: var(--gold);
    font-weight: 400;
    font-size: 16px;
    line-height: 18px;
  }
  .contact-icons {
    position: absolute;
    top: 445px;
    left: 0;
    width: 100%;
    display: flex;
    justify-content: center;
    align-items: center;
    gap: 4px;
  }
  .contact-rule {
    width: 52px;
    height: 1px;
    background: var(--rule-grey);
    margin: 0 4px;
  }
  .contact-icon {
    width: 25px;
    height: 25px;
    background: var(--tidewell-blue);
    border-radius: 3px;
    display: flex;
    align-items: center;
    justify-content: center;
  }
  .contact-details {
    position: absolute;
    top: 477px;
    left: 0;
    width: 100%;
    margin: 0;
    text-align: center;
    color: var(--ink);
    font-size: 16.5px;
    line-height: 21px;
    font-weight: 400;
  }
</style>
</head>
<body>
<div class="canvas">

  <section class="card card--back">
    <h2 class="network-heading">THE TIDEWELL NETWORK</h2>
    <div class="network-rule network-rule--top"></div>
    <p class="network-description">Tidewell unites a connected<br>group of specialist<br>professional advisory<br>firms delivering expertise<br>in Strategic Advisory,<br>Capital Raising,<br>People &amp; Finance</p>
    <div class="network-rule network-rule--bottom"></div>
  </section>

  <section class="card card--front">
    <div class="brand">
      <div class="brand-mark"></div>
      <div>
        <p class="brand-name">TIDEWELL<br>GROUP</p>
        <p class="brand-tagline">Shaping Strategy. Sustaining Momentum.<br>Delivering Results.</p>
      </div>
    </div>

    <div class="person">
      <h1 class="person-name">MARCUS HALE</h1>
      <p class="person-title">MANAGING DIRECTOR</p>
    </div>

    <div class="contact-icons">
      <div class="contact-rule"></div>
      <div class="contact-icon" aria-label="Phone">
        <svg width="17" height="15" viewBox="0 0 17 15" fill="none" stroke="#fff" stroke-width="1.4">
          <path d="M1 5 Q8.5 0 16 5 L14 7 L11.5 5.5 V4 Q8.5 3 5.5 4 V5.5 L3 7 Z" fill="#fff"/>
          <rect x="4" y="8" width="9" height="6" rx="1"/>
          <circle cx="8.5" cy="11" r="1.2" fill="#fff" stroke="none"/>
        </svg>
      </div>
      <div class="contact-icon" aria-label="Email">
        <svg width="17" height="13" viewBox="0 0 17 13" fill="none" stroke="#fff" stroke-width="1.3">
          <rect x="1" y="1" width="15" height="11"/>
          <path d="M1 1 L8.5 7.5 L16 1 M1 12 L6.5 6 M16 12 L10.5 6"/>
        </svg>
      </div>
      <div class="contact-icon" aria-label="Website">
        <svg width="17" height="17" viewBox="0 0 17 17" fill="none" stroke="#fff" stroke-width="1.3">
          <circle cx="8.5" cy="8.5" r="7"/>
          <ellipse cx="8.5" cy="8.5" rx="3" ry="7"/>
          <path d="M1.5 8.5 H15.5"/>
        </svg>
      </div>
      <div class="contact-rule"></div>
    </div>

    <p class="contact-details">055-987 654 321<br>hello@tidewellgroup.com<br>www.tidewellgroup.com</p>
  </section>

</div>
</body>
</html>
```